3 x DIN A4 Flyer, Vorder- und Rückseite
Zielgruppe
Handwerksunternehmen
Aufgabenstellung
Wir benötigen 3 Werbeflyer die in Zeitschriften beigelegt werden. Jeweils DIN A4, Vorderseite beschreibt das Produkt, Rückseite kann zur Bestellung mittels Faxantwort benutzt werden. Profibilder und Text wird vollständig geliefert.

```html
<!DOCTYPE html>
<html lang="de">
<head>
<meta charset="utf-8">
<title>Infokiste – Bestellfax</title>
<link rel="stylesheet" href="https://fonts.googleapis.com/css2?family=Open+Sans:wght@400;600;700;800&display=swap">
<style>
  :root {
    --page-bg: #e6e8ea;
    --brand-blue: #1aa3dc;
    --band-blue: #d6edf7;
    --paper: #ffffff;
    --ink: #111111;
    --ink-grey: #6d6e70;
    --field-grey: #e3e4e5;
    --field-line: #8a8b8d;
  }
  * { box-sizing: border-box; margin: 0; padding: 0; }
  html, body { width: 933px; height: 1200px; overflow: hidden; }
  body {
    background: var(--page-bg);
    font-family: "Open Sans", Arial, sans-serif;
    color: var(--ink);
  }
  .flyer {
    position: absolute; left: 60px; top: 28px;
    width: 812px; height: 1144px;
    background: var(--brand-blue);
    padding: 24px 24px 24px;
  }
  .sheet {
    width: 764px; height: 1096px;
    background: var(--paper);
    border-radius: 10px;
    overflow: hidden;
    display: flex; flex-direction: column;
  }
  .section { position: relative; }
  .header { height: 140px; background: var(--paper); }
  .recipient { height: 274px; background: var(--band-blue); }
  .orderer { height: 320px; background: var(--paper); }
  .order { flex: 1; background: var(--band-blue); }

  .brand { position: absolute; left: 44px; top: 30px; }
  .brand-name { font-size: 40px; font-weight: 800; letter-spacing: -0.5px; line-height: 1; color: var(--ink); }
  .brand-tagline { font-size: 22px; font-weight: 700; color: var(--ink-grey); line-height: 1.1; margin-top: 2px; }

  .fax-head { position: absolute; right: 50px; top: 28px; text-align: right; }
  .fax-title { font-size: 38px; font-weight: 800; color: var(--brand-blue); line-height: 1; }
  .fax-line { display: flex; align-items: center; justify-content: flex-end; gap: 10px; margin-top: 8px; }
  .fax-label { font-size: 16px; font-weight: 600; color: var(--brand-blue); }
  .fax-number { font-size: 23px; font-weight: 700; color: var(--ink); }

  .section-title {
    position: absolute; right: 50px;
    font-size: 28px; font-weight: 800; color: var(--brand-blue); line-height: 1;
  }
  .recipient .section-title { top: 26px; }
  .orderer .section-title { top: 34px; }

  .address {
    position: absolute; left: 48px; top: 44px;
    font-size: 18px; font-weight: 700; color: var(--ink-grey); line-height: 24px;
  }
  .address p + p { margin-top: 18px; }

  .subhead {
    position: absolute; left: 44px; top: 54px;
    font-size: 19px; font-weight: 800; color: var(--brand-blue);
  }
  .field { position: absolute; width: 320px; }
  .field-bar { height: 26px; background: var(--field-grey); border-bottom: 1.5px solid var(--field-line); }
  .field-label { font-size: 14px; color: var(--ink); margin-top: 6px; }
  .col-left { left: 44px; }
  .col-right { left: 396px; }

  .check { position: absolute; left: 46px; top: 92px; display: flex; gap: 16px; }
  .check-text { font-size: 19px; font-weight: 800; color: var(--ink-grey); line-height: 20px; margin-top: -4px; }
  .check-text .product { font-size: 25px; color: var(--ink); line-height: 26px; display: block; }

  .qty { position: absolute; left: 392px; top: 76px; }
  .qty-label { font-size: 14px; margin-bottom: 8px; }
  .qty-box { width: 166px; height: 50px; background: var(--field-grey); border-bottom: 1.5px solid var(--field-line); }

  .sign { top: 228px; }
  .sign .field-bar { height: 64px; }
  .sign.col-right { left: 392px; width: 324px; }
</style>
</head>
<body>
<div class="flyer">
  <div class="sheet">
    <header class="section header">
      <div class="brand">
        <div class="brand-name">INFOKISTE</div>
        <div class="brand-tagline">FÜR DIE BAUSTELLE</div>
      </div>
      <div class="fax-head">
        <div class="fax-title">BESTELLFAX</div>
        <div class="fax-line">
          <span class="fax-label">SENDEN AN</span>
          <svg width="30" height="18" viewBox="0 0 30 18" aria-hidden="true">
            <path d="M0 6h17V0l13 9-13 9v-6H0z" fill="var(--brand-blue)"/>
          </svg>
          <span class="fax-number">089 55501-100</span>
        </div>
      </div>
    </header>

    <section class="section recipient">
      <h2 class="section-title">EMPFÄNGER</h2>
      <div class="address">
        <p>KLTR mbH<br>Lindenweg 24<br>80999 München</p>
        <p>Telefon: 089 55501-140<br>Fax: 089 55501-100</p>
        <p>Ansprechpartner: Jonas Ferber</p>
      </div>
    </section>

    <section class="section orderer">
      <h3 class="subhead">IHRE ANGABEN</h3>
      <h2 class="section-title">BESTELLER</h2>
      <div class="field col-left" style="top:88px"><div class="field-bar"></div><div class="field-label">Name der Firma</div></div>
      <div class="field col-right" style="top:88px"><div class="field-bar"></div><div class="field-label">Name, Vorname</div></div>
      <div class="field col-left" style="top:152px"><div class="field-bar"></div><div class="field-label">Straße, Hausnummer</div></div>
      <div class="field col-right" style="top:152px"><div class="field-bar"></div><div class="field-label">PLZ und Ort</div></div>
      <div class="field col-left" style="top:216px"><div class="field-bar"></div><div class="field-label">Telefon</div></div>
      <div class="field col-right" style="top:216px"><div class="field-bar"></div><div class="field-label">Sie sind in welcher Innung Mitglied ?</div></div>
    </section>

    <section class="section order">
      <div class="check">
        <svg width="44" height="40" viewBox="0 0 44 40" aria-hidden="true">
          <rect x="2" y="8" width="30" height="30" fill="none" stroke="var(--ink-grey)" stroke-width="3"/>
          <path d="M8 22l8 8L40 3" fill="none" stroke="var(--brand-blue)" stroke-width="6" stroke-linejoin="round"/>
        </svg>
        <div class="check-text">ICH MÖCHTE DIE<span class="product">INFOKISTE</span>BESTELLEN</div>
      </div>
      <div class="qty">
        <div class="qty-label">Stückzahl</div>
        <div class="qty-box"></div>
      </div>
      <div class="field sign col-left"><div class="field-bar"></div><div class="field-label">Ort und Datum</div></div>
      <div class="field sign col-right"><div class="field-bar"></div><div class="field-label">Unterschrift / Stempel</div></div>
    </section>
  </div>
</div>
</body>
</html>
```